Business Cards Needed

Hi designers, I have a new logo that was created by one of the PixelHarbor designers. I'd now like to use that logo to make business cards. The company is called CarewiseMetrics Advisory and is a business consulting firm. I'd like the business cards to be horizontal, modern, and professional.
I'd like the following information to be on the business card:
1) Logo
2) my name - Janine Oulton
3) my title - Principal
4) name of business - CarewiseMetrics Advisory
5) mobile - 508.742.3391
6) e-mail - janine@carewisemetricsadvisory.example
I'm uploading a JPG file of the logo. I'm hoping this is the correct file format. Please let me know if you need another type of file. Thank you.

```html
<!DOCTYPE html>
<html lang="en">
<head>
<meta charset="utf-8">
<title>CarewiseMetrics Advisory – Business Cards</title>
<link href="https://fonts.googleapis.com/css2?family=Montserrat:wght@400;500;700&display=swap" rel="stylesheet">
<style>
  :root {
    --brand-blue: #1b6fbd;
    --brand-green: #8cc63f;
    --ink: #2b2b2b;
    --card: #ffffff;
    --backdrop: #e9ebee;
  }
  * { box-sizing: border-box; margin: 0; padding: 0; }
  html, body { width: 1200px; height: 913px; overflow: hidden; }
  body {
    background: var(--backdrop);
    font-family: "Montserrat", Arial, sans-serif;
    position: relative;
  }
  .card {
    position: absolute;
    width: 600px;
    height: 343px;
    background: var(--card);
    border-radius: 22px;
    border-bottom: 5px solid var(--brand-green);
    box-shadow: 0 10px 28px rgba(0,0,0,0.18);
  }
  .card--front { left: 90px; top: 70px; }
  .card--back { left: 510px; top: 500px; }

  .wordmark {
    display: flex;
    align-items: center;
    gap: 14px;
    color: var(--brand-blue);
    font-weight: 500;
    white-space: nowrap;
  }
  .wordmark__dot {
    border-radius: 50%;
    background: var(--brand-blue);
    flex: none;
  }
  .card--front .wordmark {
    position: absolute;
    left: 0; right: 0; top: 0; bottom: 0;
    justify-content: center;
    font-size: 34px;
  }
  .card--front .wordmark__dot { width: 26px; height: 26px; }

  .card--back .wordmark {
    position: absolute;
    left: 28px;
    top: 150px;
    font-size: 16px;
    gap: 8px;
  }
  .card--back .wordmark__dot { width: 14px; height: 14px; }

  .divider {
    position: absolute;
    left: 292px;
    top: 58px;
    width: 2px;
    height: 226px;
    background: var(--brand-blue);
  }
  .contact {
    position: absolute;
    left: 312px;
    top: 58px;
    right: 16px;
  }
  .contact__name {
    font-weight: 700;
    font-size: 24px;
    color: var(--brand-blue);
    line-height: 1.1;
  }
  .contact__name .surname { color: var(--brand-green); }
  .contact__title {
    font-size: 15px;
    color: var(--brand-blue);
    margin-top: 4px;
  }
  .contact__address {
    font-size: 14px;
    color: var(--ink);
    line-height: 1.45;
    margin-top: 16px;
  }
  .contact__list {
    list-style: none;
    margin-top: 14px;
    font-size: 12px;
    color: var(--ink);
  }
  .contact__list li {
    display: flex;
    align-items: center;
    gap: 7px;
    margin-bottom: 7px;
    white-space: nowrap;
  }
  .contact__list svg { width: 13px; height: 13px; flex: none; fill: var(--brand-blue); }
  .contact__phone { font-size: 14px; }
</style>
</head>
<body>
  <section class="card card--front" aria-label="Card front">
    <div class="wordmark"><span class="wordmark__dot"></span>CarewiseMetrics Advisory</div>
  </section>

  <section class="card card--back" aria-label="Card back">
    <div class="wordmark"><span class="wordmark__dot"></span>CarewiseMetrics Advisory</div>
    <div class="divider"></div>
    <div class="contact">
      <p class="contact__name">Janine <span class="surname">Oulton</span></p>
      <p class="contact__title">Principal</p>
      <p class="contact__address">Your address, City<br>State, Zip 1234</p>
      <ul class="contact__list">
        <li class="contact__phone">
          <svg viewBox="0 0 16 16" aria-hidden="true"><path d="M3.5 1.5l2.5 0 1 3.2-1.6 1.2a8 8 0 0 0 4.7 4.7l1.2-1.6 3.2 1v2.5a1.5 1.5 0 0 1-1.6 1.5A13 13 0 0 1 2 3.1 1.5 1.5 0 0 1 3.5 1.5z"/></svg>
          508.742.3391
        </li>
        <li>
          <svg viewBox="0 0 16 16" aria-hidden="true"><path d="M1 3h14v10H1z M2.2 4.2v.4L8 8.8l5.8-4.2v-.4z" fill-rule="evenodd"/></svg>
          janine@carewisemetricsadvisory.example
        </li>
        <li>
          <svg viewBox="0 0 16 16" aria-hidden="true"><circle cx="8" cy="8" r="7"/><path d="M1 8h14M8 1c-3 3.5-3 10.5 0 14M8 1c3 3.5 3 10.5 0 14" stroke="#fff" stroke-width="1" fill="none"/></svg>
          www.carewisemetricsadvisory.example
        </li>
      </ul>
    </div>
  </section>
</body>
</html>
```